New logo and wordpress design for Brightmoor-hub.org

We run a website that collates profiles/interviews of individuals who have completed a PhD and moved away from a traditional academix career path into something related. This is often related to the field they studied in, such as publishing, government policy, consulting, teaching and many other things. The website https://brightmoor-hub.org aims to give students and researchers ideas about what paths they can take their career on.

We would like to refresh our brand with a new website and logo. Our website is run through wordpress and hence we would need appropriate files and designs to accomodate this.
Our new logo should represent the idea of navigating a career path and exploring the unknown. Up until now it has been a compass in tones of purple and blue. We are happy to keep this motif but would need an updated, more representative logo. We are also happy to get some new ideas if the designer has something they think would fit.
The website itself should have fresh and clean look. We would like a banner at the top with clear links to the various parts of the site. The banner should stay consistent throughout the site.
We would like the main page to have a clean and simple look which places the focus on the profiles and their associated photos.
We would like pictographs to represent the different fields which our profiles fit into and would like to discuss with the winning designer what these would look like exactly. As a starting point we would like pictographs representing STEM (Science, Technology, Engineering, Mathematics) and SHAPE (Social Sciences, Humanities and Arts for People and the Economy).

We are really looking for something that is clean and professional but embodies our mission to represent all of the major industries which doctoral graduates can go on to work in. Those being, academia (universities), government, industry (private enterprise and companies), and third sector (Charities and think tanks etc.). Any design should cover all of these and not focus just on a big business or similar. It should also represent that we are not purely science focused, but all disciplines and are a broad church in that sense. We are open to various colour schemes and ideas but would like something that gives a professional but approachable feel, it should have elements of Oxford, but not suggest that we are only open to Calderwick University students or graduates.
Some sites that may be useful are:
https://kestrelguild.org/news-resources/projects/research-culture/ - talks about the different areas of employment we are trying to represent
https://www.famden-lv.ac.uk/ an oxford internal website that we like the presentation of.

Target Market(s)

Academic researchers with a PhD

Industry/Entity Type

Academic Careers

Colors
0054AA
0677BA
7BADD7
CADEEF
E8F1F8
00AB8E
00BBA5
67D7C9
C6EFE9
E9F9F6
FFF300
FFF600
FEFA6F
FFFEC7
FFFEE8
6B429C
8869AF
B7A5CE
E3DAEB
F3F0F8

Requirements
Must have
• A new logo
Should not have
• The existing logo

```html
<!DOCTYPE html>
<html lang="en">
<head>
<meta charset="utf-8">
<title>Brightmoor Hub — Explore your options beyond academia</title>
<link rel="stylesheet" href="https://fonts.googleapis.com/css2?family=Poppins:wght@300;400;500;600&display=swap">
<style>
:root{
  --indigo:#433a8c;
  --indigo-deep:#362f78;
  --blue:#4d72c0;
  --blue-soft:#6b8fd4;
  --ink:#232323;
  --text:#3d3d3d;
  --muted:#6a6a6a;
  --line:#c9c6dd;
  --footer:#2d2b30;
  --white:#ffffff;
}
*{box-sizing:border-box;margin:0;padding:0}
html,body{width:1200px;height:5324px;overflow:hidden}
body{position:relative;background:var(--white);font-family:'Poppins',sans-serif;color:var(--text)}
.abs{position:absolute}
a{color:inherit;text-decoration:none}

/* header */
.topbar{left:481px;top:0;width:719px;height:45px;background:linear-gradient(90deg,var(--indigo) 0,var(--indigo) 42%,var(--blue) 42%,var(--blue-soft) 100%);border-bottom-left-radius:30px}
.topbar .search{position:absolute;left:60px;top:14px;font-size:12px;color:#e8e6f5;letter-spacing:.5px}
.topbar .search svg{position:absolute;left:190px;top:-2px}
.topbar .contact{position:absolute;left:455px;top:14px;font-size:12px;color:#fff;letter-spacing:.5px}
.brand{left:80px;top:52px;display:flex;align-items:center;gap:10px;font-size:20px;color:var(--indigo);font-weight:400}
.brand .mark{width:52px;height:52px;border-radius:50%;background:var(--indigo)}
.nav{left:511px;top:79px;display:flex;gap:30px;font-size:12px;color:#333}
.nav .active{color:var(--indigo);font-weight:600}

/* hero */
.hero{left:0;top:129px;width:1200px;height:753px;background:linear-gradient(100deg,#6d5a4d 0%,#a89686 22%,#d9d6d8 45%,#eeeef2 62%,#f2f2f4 100%)}
.hero-copy{left:640px;top:300px;width:520px}
.hero-copy h1{font-weight:400;font-size:59px;line-height:70px;color:var(--ink);letter-spacing:.5px}
.hero-copy h1 span{color:var(--blue);font-weight:500}
.hero-copy p{margin-top:28px;font-size:18px;line-height:27px;color:#222}

.btn{display:inline-flex;align-items:center;gap:14px;border-radius:40px;background:linear-gradient(90deg,var(--indigo-deep),var(--blue-soft));color:#fff;font-weight:500;letter-spacing:.5px;white-space:nowrap}
.btn .dot{border-radius:50%;background:#fff;flex:none}
.btn-lg{height:72px;padding:0 18px 0 28px;font-size:17px}
.btn-lg .dot{width:42px;height:42px}
.btn-sm{height:60px;padding:0 14px 0 24px;font-size:14px}
.btn-sm .dot{width:34px;height:34px}

/* section titles */
.title{font-weight:400;color:var(--ink)}
.rule{height:3px;background:var(--indigo)}

/* career profiles */
.profiles-title{left:0;width:1200px;top:990px;text-align:center;font-size:68px}
.profiles-sub{left:0;width:1200px;top:1080px;text-align:center;font-size:21px;color:#1f1f1f}
.profiles-intro{left:160px;width:880px;top:1172px;text-align:center;font-size:13px;line-height:23px;color:#444}
.orbit{left:333px;top:1353px}
.hub{left:415px;top:1435px;width:372px;height:372px;border-radius:50%;background:#fff;box-shadow:0 0 40px rgba(60,50,120,.12);text-align:center;padding-top:82px;font-size:13px;line-height:23px;color:#333}
.hub strong{display:block;font-size:18px;font-weight:600;color:#1a1a1a;line-height:26px}
.face{width:136px;height:136px;border-radius:50%;border:3px solid #fff;box-shadow:0 2px 8px rgba(0,0,0,.15)}
.face.featured{width:146px;height:146px;border:5px solid var(--indigo)}

/* explore panel */
.explore{left:103px;top:2187px;width:985px;height:248px;border-radius:28px;background:var(--indigo)}
.explore .label{position:absolute;top:66px;font-size:16px;color:#fff;letter-spacing:.5px}
.explore .field{position:absolute;top:103px;height:74px;border-radius:40px;background:#fff;font-size:13px;color:#333;padding:28px 34px}
.explore .field svg{position:absolute;right:36px;top:27px}

/* get involved */
.gi-title{left:76px;top:2572px;font-size:58px}
.h-sub{font-size:19px;font-weight:500;color:var(--indigo);letter-spacing:.5px}
.body-s{font-size:13px;line-height:23px;color:#333}
.checks{left:74px;top:2886px;list-style:none}
.checks li{display:flex;align-items:flex-start;gap:8px;font-size:13px;line-height:17px;color:#333;height:33px;width:500px}
.checks li svg{flex:none}
.gi-photo{left:646px;top:2610px;width:475px;height:355px;border-radius:26px;background:linear-gradient(135deg,#3a3f48 0%,#6e7683 45%,#d9dde2 100%)}
.employers{left:728px;top:2850px;width:400px;height:330px;background:#fff;border-top-left-radius:30px;padding:50px 0 0 50px}

/* about */
.about-photo{left:74px;top:3331px;width:459px;height:448px;border-radius:28px;background:linear-gradient(180deg,#b9cde6 0%,#c6b499 45%,#8a6d49 100%)}
.about-title{left:626px;top:3338px;font-size:58px}

/* resources */
.res-title{left:0;width:1200px;top:3935px;text-align:center;font-size:62px}
.arrow{width:44px;height:44px;border-radius:50%;display:flex;align-items:center;justify-content:center}
.card{width:340px}
.card .img{width:326px;height:250px;background:linear-gradient(135deg,#9aa4b1,#e9ecf0 60%,#c3c9d1)}
.card .box{position:relative;margin:-66px 0 0 70px;background:#fff;padding:14px 0 0 0;width:280px}
.card h3{font-size:18px;font-weight:600;color:var(--indigo);line-height:23px}
.card p{margin-top:8px;font-size:12px;line-height:21px;color:#333}
.card .more{display:block;margin-top:18px;font-size:12px;font-weight:600;font-style:italic;color:var(--indigo);text-decoration:underline}

/* footer */
.footer{left:0;top:4799px;width:1200px;height:448px;background:var(--footer)}
.tags{left:74px;top:4613px;width:1047px;height:351px;border-radius:30px;background:#fff;box-shadow:0 0 0 1px #e4e2ee}
.tag{position:absolute;width:176px;height:54px;border-radius:30px;border:2px solid var(--indigo);display:flex;align-items:center;justify-content:center;font-size:17px;color:#222}
.fcol h4{font-size:22px;font-weight:400;color:#fff}
.fcol .rule{width:44px;height:2px;background:var(--blue-soft);margin-top:10px}
.fcol ul{list-style:none;margin-top:30px}
.fcol li{font-size:12px;color:#ddd;height:29px;display:flex;align-items:center;gap:8px}
.fcol li i{width:9px;height:9px;border-radius:50%;background:var(--blue-soft)}
.bottom{left:0;top:5247px;width:1200px;height:77px;background:linear-gradient(90deg,var(--indigo-deep),var(--blue-soft))}
</style>
</head>
<body>

<header>
  <div class="abs topbar">
    <span class="search">SEARCH
      <svg width="20" height="20" viewBox="0 0 20 20"><circle cx="8" cy="8" r="6" fill="none" stroke="#cfcbe8" stroke-width="2"/><line x1="12.5" y1="12.5" x2="18" y2="18" stroke="#cfcbe8" stroke-width="2"/></svg>
    </span>
    <a class="contact" href="#">CONTACT US</a>
  </div>
  <div class="abs brand"><span class="mark"></span>Brightmoor Hub</div>
  <nav class="abs nav">
    <a class="active" href="#">HOME</a><a href="#">CAREER PROFILES</a><a href="#">GET INVOLVED</a><a href="#">EVENTS</a><a href="#">RESOURCES</a><a href="#">ABOUT US</a>
  </nav>
</header>

<section>
  <div class="abs hero" role="img" aria-label="Photo of a researcher in glasses thinking at a laptop in a bright office"></div>
  <div class="abs hero-copy">
    <h1>EXPLORE YOUR<br>OPTIONS <span>BEYOND</span><br>ACADEMIA</h1>
    <p>A collection of profiles of people who have made the transition from academia to industry.</p>
    <a class="btn btn-lg" href="#" style="margin-top:34px">CONTACT US <span class="dot"></span></a>
  </div>
</section>

<section>
  <h2 class="abs title profiles-title">Career profiles</h2>
  <p class="abs profiles-sub">Researchers find all sorts of rewarding careers – smart people work everywhere!</p>
  <div class="abs rule" style="left:542px;top:1134px;width:116px"></div>
  <p class="abs profiles-intro">Such diversity in potential roles can prove challenging when exploring your options. This collection of career profiles enables you to see what others in your position chose to do, why and how they made the move, and what they most enjoy about their job.</p>

  <svg class="abs orbit" width="560" height="560" viewBox="0 0 560 560">
    <circle cx="268" cy="268" r="268" fill="none" stroke="#b8b3d6" stroke-width="1.5"/>
    <path d="M260 81 L276 81 L268 91 Z" fill="var(--indigo)"/>
    <circle cx="268" cy="103" r="2.5" fill="var(--indigo)"/><circle cx="268" cy="113" r="2.5" fill="var(--indigo)"/><circle cx="268" cy="123" r="2.5" fill="var(--indigo)"/>
  </svg>
  <div class="abs hub">
    CAREER PROFILES: PHD/<br>CONSULTING /<br>INTERDISCIPLINARY/<br>BIOSCIENCE<br>LEFT ACADEMIA AFTER: 0-3<br>YEARS POSTDOC<br>SECTOR: CONSULTING
    <strong>Liesbet Varkemaat</strong>
    Senior Consultant at<br>Verdant Metrics
  </div>
  <div class="abs face featured" style="left:528px;top:1259px;background:linear-gradient(160deg,#c9a574,#e8d3be)" role="img" aria-label="Portrait of Liesbet Varkemaat"></div>
  <div class="abs face" style="left:700px;top:1320px;background:linear-gradient(160deg,#3f3a36,#d8c3b2)" role="img" aria-label="Profile portrait"></div>
  <div class="abs face" style="left:803px;top:1454px;background:linear-gradient(160deg,#4b3528,#e3c8b6)" role="img" aria-label="Profile portrait"></div>
  <div class="abs face" style="left:824px;top:1625px;background:linear-gradient(160deg,#3c5a3a,#caa796)" role="img" aria-label="Profile portrait"></div>
  <div class="abs face" style="left:723px;top:1764px;background:linear-gradient(160deg,#6d5c4c,#e0c0a6)" role="img" aria-label="Profile portrait"></div>
  <div class="abs face" style="left:556px;top:1844px;background:linear-gradient(160deg,#2b211d,#d9b7a1 70%,#b32d30)" role="img" aria-label="Profile portrait"></div>
  <div class="abs face" style="left:380px;top:1795px;background:linear-gradient(160deg,#2e2622,#dcc1b1)" role="img" aria-label="Profile portrait"></div>
  <div class="abs face" style="left:271px;top:1660px;background:linear-gradient(160deg,#9aa7b6,#d7b59b 60%,#2e4d86)" role="img" aria-label="Profile portrait"></div>
  <div class="abs face" style="left:267px;top:1487px;background:linear-gradient(160deg,#b98b5c,#e8c9b0)" role="img" aria-label="Profile portrait"></div>
  <div class="abs face" style="left:353px;top:1332px;background:linear-gradient(160deg,#2f2824,#c9a287 60%,#eaeaea)" role="img" aria-label="Profile portrait"></div>

  <a class="abs btn btn-lg" href="#" style="left:481px;top:2034px;width:260px;padding:0 14px 0 26px;font-size:15px;justify-content:space-between">VIEW ALL PROFILES <span class="dot"></span></a>

  <div class="abs explore">
    <span class="label" style="left:142px">EXPLORE CAREER PROFILES</span>
    <span class="label" style="left:540px">RECENT PROFILES</span>
    <div class="field" style="left:134px;width:331px">Select Catagory
      <svg width="12" height="10" viewBox="0 0 12 10"><path d="M1 1 L11 1 L6 9 Z" fill="var(--indigo)"/></svg>
    </div>
    <div class="field" style="left:517px;width:332px">Search
      <svg width="20" height="20" viewBox="0 0 20 20"><circle cx="8" cy="8" r="6" fill="none" stroke="var(--indigo)" stroke-width="2"/><line x1="12.5" y1="12.5" x2="18" y2="18" stroke="var(--indigo)" stroke-width="2"/></svg>
    </div>
  </div>
</section>

<section>
  <h2 class="abs title gi-title">Get Involved</h2>
  <div class="abs rule" style="left:76px;top:2660px;width:66px"></div>
  <h3 class="abs h-sub" style="left:74px;top:2719px">RESEARCHERS</h3>
  <p class="abs body-s" style="left:74px;top:2770px;width:500px">Are you a researcher keen to know more about roles beyond academia? And to extend your professional network?</p>
  <p class="abs body-s" style="left:74px;top:2834px">As a member of the editorial team, you will be</p>
  <ul class="abs checks">
    <li><svg width="18" height="18" viewBox="0 0 18 18"><circle cx="9" cy="9" r="7.5" fill="none" stroke="var(--indigo)" stroke-width="1.8"/><path d="M5 9 L8 12 L16 3" fill="none" stroke="var(--indigo)" stroke-width="2"/></svg>Able to expand the collection in sectors of interest to you</li>
    <li><svg width="18" height="18" viewBox="0 0 18 18"><circle cx="9" cy="9" r="7.5" fill="none" stroke="var(--indigo)" stroke-width="1.8"/><path d="M5 9 L8 12 L16 3" fill="none" stroke="var(--indigo)" stroke-width="2"/></svg>Supported by fellow team-members and the Careers Service</li>
    <li><svg width="18" height="18" viewBox="0 0 18 18"><circle cx="9" cy="9" r="7.5" fill="none" stroke="var(--indigo)" stroke-width="1.8"/><path d="M5 9 L8 12 L16 3" fill="none" stroke="var(--indigo)" stroke-width="2"/></svg>Networking effectively in circles relevant to you</li>
    <li><svg width="18" height="18" viewBox="0 0 18 18"><circle cx="9" cy="9" r="7.5" fill="none" stroke="var(--indigo)" stroke-width="1.8"/><path d="M5 9 L8 12 L16 3" fill="none" stroke="var(--indigo)" stroke-width="2"/></svg>Broadening your communication skills and commercial awareness in ways valued by future employers</li>
  </ul>
  <a class="abs btn btn-sm" href="#" style="left:78px;top:3059px">CONTACT US <span class="dot"></span></a>

  <div class="abs gi-photo" role="img" aria-label="Photo of hands typing on a laptop beside a keyboard"></div>
  <div class="abs employers">
    <h3 class="h-sub">EMPLOYERS</h3>
    <p class="body-s" style="margin-top:18px;width:345px">Do you want to raise your profile amongst researchers?</p>
    <p class="body-s" style="margin-top:12px;width:345px">It is easy and quick to submit an employee profile to brightmoor-hub.org, and accompany this with a brief outline of your organisation.</p>
    <p class="body-s" style="margin-top:12px;width:345px">PhD students and research staff keen to look beyond academia are increasingly using this site to consider their options.</p>
  </div>
</section>

<section>
  <div class="abs about-photo" role="img" aria-label="Photo of a domed historic university library building"></div>
  <h2 class="abs title about-title">About Us</h2>
  <h3 class="abs h-sub" style="left:627px;top:3415px;font-size:15px">WHO WE ARE</h3>
  <p class="abs body-s" style="left:626px;top:3477px;width:475px">We, the editors, are a team of curious and committed volunteer PhD students and research staff working in partnership with the Calderwick University Careers Service. Our role is to source career profiles from a range of fascinating sectors written by researchers with backgrounds spanning the humanities, social sciences, physical and life sciences.</p>
  <a class="abs btn btn-sm" href="#" style="left:624px;top:3625px">CONTACT US <span class="dot"></span></a>
</section>

<section>
  <h2 class="abs title res-title">Resources</h2>
  <div class="abs rule" style="left:527px;top:4033px;width:146px"></div>
  <div class="abs arrow" style="left:1023px;top:4089px;background:#fff;box-shadow:0 1px 6px rgba(0,0,0,.2)">
    <svg width="18" height="12" viewBox="0 0 18 12"><path d="M17 6 H2 M6 1 L1 6 L6 11" fill="none" stroke="#333" stroke-width="2"/></svg></div>
  <div class="abs arrow" style="left:1079px;top:4089px;background:var(--indigo)">
    <svg width="18" height="12" viewBox="0 0 18 12"><path d="M1 6 H16 M12 1 L17 6 L12 11" fill="none" stroke="#fff" stroke-width="2"/></svg></div>

  <article class="abs card" style="left:81px;top:4159px">
    <div class="img" role="img" aria-label="Photo of a researcher holding a folder in a corridor"></div>
    <div class="box"><h3>Stepwise. Unlocking postdoc career potential</h3>
      <p>A new approach to postdoc career development: a portal of free, accessible,</p><a class="more" href="#">READ MORE</a></div>
  </article>
  <article class="abs card" style="left:438px;top:4159px">
    <div class="img" role="img" aria-label="Photo of two scientists discussing work in a laboratory"></div>
    <div class="box"><h3>Kestrel Guild: Career Case Studies</h3>
      <p>A collection of case studies highlighting the range of career paths taken by researchers</p><a class="more" href="#">READ MORE</a></div>
  </article>
  <article class="abs card" style="left:799px;top:4159px">
    <div class="img" role="img" aria-label="Photo of colleagues working at laptops in an open office"></div>
    <div class="box"><h3>Lumenpath: What do researcher staff do next?</h3>
      <p>Career stories collection describing the experiences of research staff who have moved</p><a class="more" href="#">READ MORE</a></div>
  </article>
</section>

<footer>
  <div class="abs footer"></div>
  <div class="abs tags">
    <h2 style="position:absolute;left:0;width:100%;top:30px;text-align:center;font-size:36px;font-weight:400;color:var(--indigo)">TAGS</h2>
    <div class="rule" style="position:absolute;left:491px;top:89px;width:66px;height:2px"></div>
    <span class="tag" style="left:55px;top:134px">Australia</span>
    <span class="tag" style="left:245px;top:134px">Biochemistry</span>
    <span class="tag" style="left:439px;top:134px">Biology</span>
    <span class="tag" style="left:631px;top:134px">Biotechnology</span>
    <span class="tag" style="left:821px;top:134px">Business</span>
    <span class="tag" style="left:55px;top:206px">Charity</span>
    <span class="tag" style="left:245px;top:206px">Chemistry</span>
    <span class="tag" style="left:439px;top:206px">Classics</span>
    <span class="tag" style="left:631px;top:206px">Communication</span>
    <span class="tag" style="left:821px;top:206px">Consulting</span>
    <svg style="position:absolute;left:486px;top:297px" width="80" height="10" viewBox="0 0 80 10"><circle cx="5" cy="5" r="4" fill="var(--indigo)"/><circle cx="29" cy="5" r="4" fill="#c9c6dd"/><circle cx="53" cy="5" r="4" fill="#c9c6dd"/><circle cx="77" cy="5" r="3.5" fill="#c9c6dd"/></svg>
  </div>

  <div class="abs fcol" style="left:147px;top:5010px">
    <h4>Quick links</h4><div class="rule"></div>
    <ul><li><i></i>Career Profiles</li><li><i></i>Get Involved</li><li><i></i>Events</li><li><i></i>Resources</li><li><i></i>About us</li></ul>
  </div>
  <div class="abs fcol" style="left:407px;top:5010px">
    <h4>Recent Profiles</h4><div class="rule"></div>
    <ul><li>Marisol Quenta-Arriaga June 12, 2024</li><li>Henry Dalworth May 21, 2024</li><li>Ritika Sandhval April 2, 2024</li><li>Anvi Kelkar April 2, 2024</li><li>Orhan Tezbilir March 28, 2024</li></ul>
  </div>
  <div class="abs fcol" style="left:785px;top:5010px">
    <h4>Posts from @BrightmoorPhD</h4><div class="rule"></div>
    <p style="margin-top:30px;font-size:12px;line-height:14px;color:#ddd">Nothing to see here - yet<br>When they post, their posts<br>will show up here</p>
    <a href="#" style="display:inline-flex;margin-top:20px;width:124px;height:34px;border-radius:18px;background:#1d9bf0;color:#fff;font-size:12px;align-items:center;justify-content:center">View Feed</a>
  </div>

  <div class="abs bottom">
    <p style="position:absolute;left:157px;top:30px;font-size:11px;color:#fff">Copyright © 2024 All Rights Reserved By Company name</p>
    <span style="position:absolute;left:1018px;top:20px;width:40px;height:40px;border-radius:50%;background:#1d9bf0"></span>
  </div>
</footer>

</body>
</html>
```